KB Rubbish Removal Business Card

Hey,
I need a double sided business card designed for a rubbish removal business based in Australia. Logo is already chosen, similar colours preferred for both sides of the business card.

Details to include:

Front:

KB Rubbish Removal
Darren Holloway
Managing Director
Mobile: 0471 902 146
Email: darren@kbrubbishremoval.com.au
Website: kbrubbishremoval.com.au

Rear:

How did we do?
kbrubbishremoval.com.au/review

```html
<!DOCTYPE html>
<html lang="en">
<head>
<meta charset="utf-8">
<title>KB Rubbish Removal – Business Card</title>
<link href="https://fonts.googleapis.com/css2?family=Archivo:wght@400;700;800;900&family=Roboto:wght@300;400&display=swap" rel="stylesheet">
<style>
  :root {
    --page-bg: #e9eae6;
    --lime: #dce489;
    --green: #2f9e3c;
    --green-mid: #4fb446;
    --white: #ffffff;
    --ink: #1b1b1b;
  }
  * { box-sizing: border-box; margin: 0; padding: 0; }
  html, body {
    width: 1200px; height: 1200px; overflow: hidden;
    background: var(--page-bg);
  }
  body {
    display: flex; flex-direction: column; align-items: center; justify-content: center;
    gap: 40px;
  }
  .card {
    position: relative;
    width: 960px; height: 548px;
    overflow: hidden;
    box-shadow: 0 8px 24px rgba(0,0,0,0.12);
  }
  .corner-mark {
    position: absolute; right: -110px; bottom: -110px;
    width: 260px; height: 260px; border-radius: 50%;
    background: linear-gradient(135deg, var(--green-mid), var(--green));
  }

  /* ---------- Rear ---------- */
  .card-rear { background: var(--lime); }
  .rear-heading {
    position: absolute; left: 150px; top: 70px;
    font-family: "Archivo", sans-serif; font-weight: 900;
    font-size: 88px; line-height: 1.1; color: var(--ink); letter-spacing: 0.5px;
  }
  .rear-url {
    position: absolute; left: 150px; top: 178px;
    font-family: "Roboto", sans-serif; font-weight: 400;
    font-size: 30px; color: var(--ink);
  }
  .rear-company {
    position: absolute; left: 170px; top: 370px;
    font-family: "Archivo", sans-serif; font-weight: 800;
    font-size: 46px; color: var(--ink); letter-spacing: 1px;
  }

  /* ---------- Front ---------- */
  .card-front { background: var(--white); }
  .front-panel {
    position: absolute; left: 0; top: 0; bottom: 0; width: 340px;
    background: var(--lime);
  }
  .front-stripe {
    position: absolute; left: 356px; top: 0; bottom: 0; width: 12px;
    background: var(--green);
  }
  .brand-disc {
    position: absolute; left: 252px; top: 36px;
    width: 210px; height: 210px; border-radius: 50%;
    background: var(--white);
  }
  .brand-pill {
    position: absolute; left: 40px; top: 250px;
    height: 68px; width: 330px; border-radius: 34px;
    background: var(--white);
  }
  .brand-name {
    position: absolute; left: 72px; top: 258px;
    font-family: "Archivo", sans-serif; font-weight: 800;
    font-size: 44px; line-height: 52px; color: var(--ink); letter-spacing: 1px;
    white-space: nowrap;
  }
  .contact-block {
    position: absolute; right: 60px; top: 96px;
    text-align: right; color: var(--ink);
  }
  .person-name {
    font-family: "Archivo", sans-serif; font-weight: 800;
    font-size: 40px; line-height: 1.15; letter-spacing: 1px;
  }
  .person-title {
    font-family: "Roboto", sans-serif; font-weight: 400;
    font-size: 24px; margin-top: 2px;
  }
  .person-phone {
    font-family: "Archivo", sans-serif; font-weight: 700;
    font-size: 34px; letter-spacing: 1.5px; margin-top: 4px;
    display: flex; align-items: center; justify-content: flex-end; gap: 10px;
  }
  .person-phone svg { width: 24px; height: 24px; }
  .web-block {
    position: absolute; right: 175px; bottom: 50px;
    text-align: right; color: var(--ink);
    font-family: "Roboto", sans-serif; font-weight: 400;
    font-size: 26px; line-height: 1.4; white-space: nowrap;
  }
</style>
</head>
<body>

  <section class="card card-rear" aria-label="Business card, rear side">
    <h1 class="rear-heading">How did we do?</h1>
    <p class="rear-url">kbrubbishremoval.com.au/review</p>
    <p class="rear-company">KB RUBBISH REMOVAL</p>
    <div class="corner-mark"></div>
  </section>

  <section class="card card-front" aria-label="Business card, front side">
    <div class="front-panel"></div>
    <div class="front-stripe"></div>
    <div class="brand-disc"></div>
    <div class="brand-pill"></div>
    <p class="brand-name">KB RUBBISH REMOVAL</p>

    <div class="contact-block">
      <p class="person-name">Darren Holloway</p>
      <p class="person-title">Managing Director</p>
      <p class="person-phone">
        <svg viewBox="0 0 24 24" aria-hidden="true"><path fill="#1b1b1b" d="M6.6 10.8c1.4 2.8 3.8 5.1 6.6 6.6l2.2-2.2c.3-.3.7-.4 1-.2 1.1.4 2.3.6 3.6.6.6 0 1 .4 1 1V20c0 .6-.4 1-1 1C10.6 21 3 13.4 3 4c0-.6.4-1 1-1h3.5c.6 0 1 .4 1 1 0 1.3.2 2.5.6 3.6.1.3 0 .7-.2 1l-2.3 2.2z"/></svg>
        0471 902 146
      </p>
    </div>

    <div class="web-block">
      <p>kbrubbishremoval.com.au</p>
      <p>darren@kbrubbishremoval.com.au</p>
    </div>
    <div class="corner-mark"></div>
  </section>

</body>
</html>
```